Brivtel sales folder inserts

We need the same design for 4 separate service offerings to put inside our sales folder. Each insert should be laid out the same with different images and text and the 2nd, 3rd, and 4th should each be 3/4" shorter than the previous one so that when all 4 are inserted into the folder you see the black strip with text showing what the service offering is. Basically staggered inserts.

Industry/Entity Type

Information Technology

Font styles to use
Sans Serif

Colors
acd136

Requirements
Must have
• Brivtel logo and included text. Keep with the green Pantone 90 and black color scheme
Nice to have
• a better layout and pics

```html
<!DOCTYPE html>
<html lang="en">
<head>
<meta charset="utf-8">
<title>Brivtel FULL-VAULT Insert</title>
<link rel="stylesheet" href="https://fonts.googleapis.com/css2?family=Roboto+Condensed:ital,wght@0,400;0,700;1,700&family=Roboto:wght@900&family=Oswald:wght@600&display=swap">
<style>
  :root {
    --green: #a5c63b;
    --green-bright: #acd136;
    --black: #000000;
    --ink: #1c1c1c;
    --white: #ffffff;
    --rule: #3a3a3a;
    --hero-deep: #05080c;
    --hero-mid: #0e3a52;
    --hero-glow: #7fd6ee;
  }
  * { margin: 0; padding: 0; box-sizing: border-box; }
  html, body { width: 927px; height: 1200px; overflow: hidden; background: var(--white); }
  body { font-family: "Roboto Condensed", "Arial Narrow", sans-serif; color: var(--ink); }
  .insert { position: relative; width: 927px; height: 1200px; overflow: hidden; background: var(--white); }

  .brand { position: absolute; left: 58px; top: 40px; height: 72px; display: flex; align-items: center; }
  .brand-mark { width: 52px; height: 52px; background: var(--ink); }
  .brand-divider { width: 2px; height: 76px; background: var(--ink); margin: 0 20px 0 56px; }
  .brand-name { font-size: 34px; font-weight: 700; color: var(--ink); letter-spacing: 3px; }

  .service-tab { position: absolute; right: 0; top: 0; width: 345px; height: 112px; }
  .service-tab svg { position: absolute; inset: 0; }
  .service-tab-label { position: absolute; right: 46px; top: 46px; font-family: "Oswald", "Roboto Condensed", sans-serif; font-size: 40px; font-weight: 600; color: var(--ink); letter-spacing: 1.5px; line-height: 1; }

  .hero { position: absolute; left: 0; top: 116px; width: 927px; height: 398px;
    background:
      radial-gradient(circle at 600px 250px, var(--hero-glow) 0, #2a8fb0 60px, var(--hero-mid) 150px, transparent 300px),
      linear-gradient(180deg, var(--hero-deep) 0%, #0b2233 45%, #0f3346 65%, var(--hero-deep) 100%); }
  .hero-title { position: absolute; left: 48px; top: 142px; font-family: "Roboto", sans-serif; font-weight: 900; font-size: 40px; line-height: 48px; color: var(--white); letter-spacing: -0.5px;
    text-shadow: -2px -2px 0 #111, 2px -2px 0 #111, -2px 2px 0 #111, 2px 2px 0 #111, 0 3px 0 #111; }

  .facts-column { position: absolute; left: 566px; top: 496px; width: 306px; height: 704px; }
  .facts-column svg { position: absolute; inset: 0; }

  .pill { position: absolute; left: 582px; width: 312px; height: 29px; background: var(--green); border-radius: 0 15px 15px 0; display: flex; align-items: center; }
  .pill::before { content: ""; width: 11px; height: 11px; border-radius: 50%; background: var(--black); margin: 0 8px 0 10px; }
  .pill span { font-size: 15.5px; font-weight: 700; font-style: italic; color: var(--black); letter-spacing: 0.3px; }
  .pill-questions { top: 544px; }
  .pill-facts { top: 740px; }

  .feature-list { position: absolute; left: 588px; top: 592px; width: 256px; list-style: none; }
  .feature-list li { position: relative; padding: 0 0 8px 21px; margin-bottom: 9px; font-size: 14px; line-height: 18px; letter-spacing: 0.5px; color: var(--white); border-bottom: 1px solid var(--rule); hyphens: auto; }
  .feature-list li:last-child { border-bottom: none; }
  .feature-list em { font-style: normal; font-weight: 700; color: var(--green); }

  .tick { position: absolute; left: 0; top: 1px; width: 15px; height: 14px; }

  .stat-list { position: absolute; left: 588px; top: 786px; width: 256px; list-style: none; }
  .stat-list li { position: relative; padding: 0 0 4px 21px; margin-bottom: 6px; font-size: 14px; line-height: 21px; letter-spacing: 0.5px; color: var(--white); border-bottom: 1px solid var(--rule); hyphens: auto; }
  .stat-list li:last-child { border-bottom: none; }
  .stat-list .tick { top: 10px; }
  .stat-figure { font-size: 30px; font-weight: 700; color: var(--green); line-height: 30px; margin-right: 2px; letter-spacing: 0; }

  .intro-shield { position: absolute; left: 52px; top: 552px; width: 72px; height: 80px; }
  .intro-heading { position: absolute; left: 138px; top: 544px; font-size: 32px; font-weight: 700; font-style: italic; color: var(--green); line-height: 1.1; letter-spacing: 0.3px; }
  .intro-sub { position: absolute; left: 139px; top: 590px; font-size: 25px; color: var(--ink); letter-spacing: 0.4px; }

  .body-copy { position: absolute; left: 55px; top: 652px; width: 476px; font-size: 14.5px; line-height: 18.4px; letter-spacing: 0.45px; text-align: justify; color: var(--ink); }
  .body-copy p { margin-bottom: 18.4px; }

  .tagline-band { position: absolute; left: 0; top: 1114px; width: 927px; height: 56px; background: var(--green); display: flex; align-items: center; justify-content: center; }
  .tagline-band p { font-size: 34px; font-weight: 700; font-style: italic; color: var(--white); letter-spacing: 0.8px; }
</style>
</head>
<body>
<main class="insert">

  <header>
    <div class="brand">
      <div class="brand-mark"></div>
      <div class="brand-divider"></div>
      <div class="brand-name">BRIVTEL</div>
    </div>
    <div class="service-tab">
      <svg width="345" height="112" viewBox="0 0 345 112">
        <path d="M0 0 H345 V112 H48 Q28 112 24 92 Z" fill="var(--green)"/>
      </svg>
      <div class="service-tab-label">FULL-VAULT</div>
    </div>
  </header>

  <section class="hero" role="img" aria-label="Close-up of a glowing eye surrounded by streams of blue binary code, suggesting watchful data protection">
    <h1 class="hero-title">FULL-VAULT<br>RUN ANYWHERE,<br>PROTECT ANYTHING</h1>
  </section>

  <aside class="facts-column">
    <svg width="306" height="704" viewBox="0 0 306 704">
      <path d="M0 12 Q150 -4 306 8 V704 H0 Z" fill="var(--black)"/>
    </svg>
  </aside>

  <div class="pill pill-questions"><span>Does your backup solution do this?</span></div>
  <ul class="feature-list" lang="en">
    <li><svg class="tick" viewBox="0 0 15 14"><path d="M1 8 L5 12 L14 1" fill="none" stroke="var(--green)" stroke-width="3"/></svg>Test and verify your backups by boot&shy;ing on a virtual server in the cloud</li>
    <li><svg class="tick" viewBox="0 0 15 14"><path d="M1 8 L5 12 L14 1" fill="none" stroke="var(--green)" stroke-width="3"/></svg>Backup your WorkDesk <em>365</em></li>
    <li><svg class="tick" viewBox="0 0 15 14"><path d="M1 8 L5 12 L14 1" fill="none" stroke="var(--green)" stroke-width="3"/></svg>Allow you to spin up virtual servers in the cloud during a disaster</li>
  </ul>

  <div class="pill pill-facts"><span>Did You Know?</span></div>
  <ul class="stat-list" lang="en">
    <li><svg class="tick" viewBox="0 0 15 14"><path d="M1 8 L5 12 L14 1" fill="none" stroke="var(--green)" stroke-width="3"/></svg><span class="stat-figure">60%</span> of backups are incomplete</li>
    <li><svg class="tick" viewBox="0 0 15 14"><path d="M1 8 L5 12 L14 1" fill="none" stroke="var(--green)" stroke-width="3"/></svg><span class="stat-figure">50%</span> of restores fail</li>
    <li><svg class="tick" viewBox="0 0 15 14"><path d="M1 8 L5 12 L14 1" fill="none" stroke="var(--green)" stroke-width="3"/></svg><span class="stat-figure">40%</span> of the SMB market will be attacked by a hacker, 50% wont even know it.</li>
    <li><svg class="tick" viewBox="0 0 15 14"><path d="M1 8 L5 12 L14 1" fill="none" stroke="var(--green)" stroke-width="3"/></svg><span class="stat-figure">20%</span> of SMB market will lose critical data every 5-years</li>
    <li><svg class="tick" viewBox="0 0 15 14"><path d="M1 8 L5 12 L14 1" fill="none" stroke="var(--green)" stroke-width="3"/></svg><span class="stat-figure">90%</span> of business that lost data for 10-days or more filed for bank&shy;ruptcy immediately</li>
  </ul>

  <section class="intro">
    <svg class="intro-shield" viewBox="0 0 72 80" aria-hidden="true">
      <path d="M4 6 Q36 -2 68 6 V34 Q68 62 36 78 Q4 62 4 34 Z" fill="#8a8f96" stroke="#2b2f36" stroke-width="3"/>
      <path d="M10 11 Q36 4 62 11 V34 Q62 57 36 71 Q10 57 10 34 Z" fill="#2c5aa6"/>
      <circle cx="32" cy="36" r="12" fill="#cfe9f7"/>
    </svg>
    <h2 class="intro-heading">Run Anywhere, Protect Anything</h2>
    <p class="intro-sub">Your Business Continuity Solution.</p>
  </section>

  <section class="body-copy">
    <p>Brivtel’s FULL-VAULT solution provides comprehensive backups for your data like never before.</p>
    <p>In todays environment threats are never ending. There is always a new threat trying to get to your data, whether to Krypto lock it and hold it for ransom, or be malicious and delete it for no reason at all.</p>
    <p>Keeping your network up to date and monitoring for suspicious activity are all recommended actions, but backing up your data is the most important action you can take.</p>
    <p>Don’t just back up your data. Verify it. What good is a backup of your data if it does not work when you need it. The Brivtel FULL-Vault solution tests and verifies your data on a daily basis.</p>
    <p>The FULL-Vault solution also provides you a local and an off-site copy of your data. What good is a business continuity plan if your backups burn down with your building.</p>
    <p>The FULL-Vault solution provides an onsite server resource should you need it, as well as allowing you to spin up virtual servers in the cloud during a disaster scenario.</p>
  </section>

  <footer class="tagline-band">
    <p>A Little Mistake Can Cost a Fortunea</p>
  </footer>

</main>
</body>
</html>
```